Luxury In Home Massages by five star therapist

My name is Tessa Coraline Whitby. I am a female massage therapist with many years of experience working in the luxury resort spa, in Holistic Wellness Centers and in providing the finest in- home visit massages. I am passionate about providing massages that enhance the mind/body well being of my client . I have clients who have been with me for years. My background includes owning my own Wellness Spa, specializing in prenatal, post partum massage, relaxing and rejuvenating massages (Deep Tissue, Myofascial Release, Connective Sculpting etc.) for both men and women. I am also a clinical aromatherapist and often incorporate aromatherapy in order to help with insomnia, stress, anxiety and stress that a busy lifestyle creates. I custom blend my essential oils for the needs of the client. Should one prefer scentless lotion, I use a luxury line from Valorine. I am currently open seeking to taking a few new clients in the evenings and on Sundays.I have excellent home visit references from residents of the Strands in Dana Point, Llido Isle, Nellie Gail, Newport Beach, Laguna BeachI want a very classy and elegant card with a feminine feel. Not just the same stock massage pictures I always see....This card MUST set me apart and appeal to the discerning/wealthy client

Target Market(s)

High end professionals/ homemakers/pregnant moms/

Industry/Entity Type

Health And Wellness

Font styles to use
Decorative
Script

Requirements
Must have
• A strikingly beautiful design with words connotating expertise and class.
Should not have
• a square, male look or the blah same old stock photography person on the massage table

```html
<!DOCTYPE html>
<html lang="en">
<head>
<meta charset="utf-8">
<title>Tessa Coraline Whitby – Home Visit Massage Postcard</title>
<link href="https://fonts.googleapis.com/css2?family=Mulish:ital,wght@0,300;0,400;1,300&display=swap" rel="stylesheet">
<style>
  :root{
    --cocoa:#6b4336;
    --cocoa-soft:#7a5040;
    --tan:#cf9d68;
    --cream:#fbf3ea;
    --ink-brown:#6b4336;
    --rule:#c8c8c8;
    --stage:#e9e7e4;
  }
  *{box-sizing:border-box;margin:0;padding:0}
  html,body{width:1006px;height:1200px;overflow:hidden;background:var(--stage);font-family:"Mulish",sans-serif}
  .postcard{position:absolute;left:72px;width:862px;box-shadow:0 2px 8px rgba(0,0,0,.18);overflow:hidden;background:#fff}
  .postcard--front{top:30px;height:562px}
  .postcard--back{top:618px;height:558px}
  .postcard__art{position:absolute;inset:0;width:100%;height:100%}
  .txt{position:absolute;color:var(--cream);font-weight:300;white-space:nowrap}

  /* front */
  .front__name{left:0;width:325px;top:32px;text-align:center;font-size:21px}
  .front__title{left:0;width:325px;top:80px;text-align:center;font-size:28px;line-height:36px;font-weight:300;text-transform:uppercase}
  .front__audience{left:0;width:325px;top:162px;text-align:center;font-size:11px;text-transform:uppercase}
  .front__intro{left:29px;top:200px;font-size:12px;line-height:21px;letter-spacing:-.2px}
  .services{position:absolute;left:24px;top:318px;list-style:none;color:var(--cream);font-size:12.5px;font-weight:300;line-height:21px}
  .services li{display:flex;align-items:center;gap:11px}
  .services li svg{flex:none}
  .services .services__note{padding-left:24px}
  .front__social{left:20px;top:453px;display:flex;align-items:center;gap:8px;font-size:13px}
  .front__social .dot{width:30px;height:30px;border-radius:50%;background:var(--cream);display:inline-block}
  .front__contact-name{left:24px;top:493px;font-size:14px}
  .front__contact{left:22px;top:517px;font-size:14px;display:flex;align-items:center;gap:6px}
  .badge{position:absolute;left:680px;top:22px;width:150px;height:150px;transform:rotate(9deg);text-align:center;color:var(--cream);font-weight:300}
  .badge__name{margin-top:40px;font-size:10.5px}
  .badge__claim{font-size:19px;line-height:23px}

  /* back */
  .back__title{left:0;width:400px;top:22px;text-align:center;font-size:28px;line-height:36px;font-weight:300;text-transform:uppercase}
  .back__aroma{left:0;width:400px;top:117px;text-align:center;font-size:17px}
  .back__help{left:0;width:400px;top:142px;text-align:center;font-size:15px}
  .back__signature{left:40px;top:354px;font-size:38px}
  .testimonial{position:absolute;left:26px;top:428px;display:flex;gap:8px;color:var(--cream);font-style:italic;font-weight:300;font-size:11px;line-height:16.5px}
  .testimonial__mark{font-size:34px;line-height:26px;color:var(--tan);font-style:normal}
  .back__contact-name{left:423px;top:45px;font-size:15px;color:var(--ink-brown)}
  .back__contact{left:421px;top:69px;font-size:15px;color:var(--ink-brown);display:flex;align-items:center;gap:6px}
  .stamp-box{position:absolute;left:731px;top:33px;width:100px;height:84px;border:1.5px solid var(--rule)}
  .address-line{position:absolute;left:563px;width:268px;height:0;border-top:1.5px solid var(--rule)}
</style>
</head>
<body>

<section class="postcard postcard--front">
  <svg class="postcard__art" viewBox="0 0 862 562">
    <defs>
      <linearGradient id="photoWarm" x1="0" y1="0" x2="1" y2="1">
        <stop offset="0" stop-color="#b87848"/>
        <stop offset=".35" stop-color="#c98a58"/>
        <stop offset=".65" stop-color="#e3bf98"/>
        <stop offset="1" stop-color="#f6f1ea"/>
      </linearGradient>
      <radialGradient id="photoGlow" cx=".72" cy=".35" r=".45">
        <stop offset="0" stop-color="#f2e3d0" stop-opacity=".85"/>
        <stop offset="1" stop-color="#f2e3d0" stop-opacity="0"/>
      </radialGradient>
      <radialGradient id="photoShade" cx=".55" cy=".95" r=".35">
        <stop offset="0" stop-color="#5a3527" stop-opacity=".55"/>
        <stop offset="1" stop-color="#5a3527" stop-opacity="0"/>
      </radialGradient>
      <radialGradient id="swirlGlow" cx=".5" cy=".5" r=".5">
        <stop offset="0" stop-color="#cf9d68" stop-opacity=".45"/>
        <stop offset="1" stop-color="#cf9d68" stop-opacity="0"/>
      </radialGradient>
    </defs>
    <g role="img" aria-label="Photo: therapist giving a back massage to a relaxed client, candle in the foreground">
      <rect width="862" height="562" fill="url(#photoWarm)"/>
      <rect width="862" height="562" fill="url(#photoGlow)"/>
      <rect width="862" height="562" fill="url(#photoShade)"/>
    </g>
    <path d="M0,0 H378 C300,55 285,150 360,240 C430,325 478,410 470,562 H0 Z" fill="var(--cocoa)"/>
    <path d="M378,0 C300,55 285,150 360,240 C430,325 478,410 470,562" fill="none" stroke="var(--tan)" stroke-width="4"/>
    <ellipse cx="335" cy="495" rx="75" ry="65" fill="url(#swirlGlow)" role="img" aria-label="Tan swirl ornament"/>
    <circle cx="755" cy="97" r="80" fill="var(--tan)"/>
    <circle cx="755" cy="97" r="74" fill="var(--cocoa-soft)"/>
  </svg>

  <div class="txt front__name">Tessa Coraline Whitby</div>
  <h1 class="txt front__title">Finest Home Visit<br>Massages</h1>
  <div class="txt front__audience">For men and women</div>
  <p class="txt front__intro">EXPERIENCE massage therapist with many<br>years of experience working in the luxury resort spa,<br>in Holistic Wellness Centers and in providing<br>the finest in- home visit massages.</p>
  <ul class="services">
    <li><svg width="13" height="13" viewBox="0 0 13 13"><circle cx="6.5" cy="6.5" r="5.5" fill="none" stroke="#fbf3ea"/><path d="M5 4l3 2.5L5 9" fill="none" stroke="#fbf3ea"/></svg>Prenatal</li>
    <li><svg width="13" height="13" viewBox="0 0 13 13"><circle cx="6.5" cy="6.5" r="5.5" fill="none" stroke="#fbf3ea"/><path d="M5 4l3 2.5L5 9" fill="none" stroke="#fbf3ea"/></svg>Post partum massage</li>
    <li><svg width="13" height="13" viewBox="0 0 13 13"><circle cx="6.5" cy="6.5" r="5.5" fill="none" stroke="#fbf3ea"/><path d="M5 4l3 2.5L5 9" fill="none" stroke="#fbf3ea"/></svg>Relaxing and rejuvenating massages</li>
    <li class="services__note">(Deep Tissue, Myofascial Release, Connective Sculpting etc.)</li>
  </ul>
  <div class="txt front__social"><span class="dot"></span>Proflink</div>
  <div class="txt front__contact-name">Tessa Coraline Whitby</div>
  <div class="txt front__contact">Contact me on
    <svg width="18" height="18" viewBox="0 0 18 18"><circle cx="9" cy="9" r="8" fill="none" stroke="#fbf3ea" stroke-width="1.3"/><path d="M6 5c-1 1 0 4 2 6s5 3 6 2l-1.5-1.5-1.5 1c-1-.5-2.5-2-3-3l1-1.5z" fill="#fbf3ea"/></svg>
    000 0000 000</div>
  <div class="badge">
    <div class="badge__name">Tessa Coraline Whitby</div>
    <div class="badge__claim">Over 20 years<br>of experience</div>
  </div>
</section>

<section class="postcard postcard--back">
  <svg class="postcard__art" viewBox="0 0 862 558">
    <defs>
      <clipPath id="leftPanel">
        <path d="M0,0 H432 C395,45 385,120 420,195 C470,300 535,370 528,460 C524,510 500,540 470,558 H0 Z"/>
      </clipPath>
      <linearGradient id="candleBase" x1="0" y1="0" x2="0" y2="1">
        <stop offset="0" stop-color="#8a5a3e"/>
        <stop offset=".55" stop-color="#6e4634"/>
        <stop offset="1" stop-color="#4a2f24"/>
      </linearGradient>
      <radialGradient id="candleGlow" cx=".3" cy=".6" r=".45">
        <stop offset="0" stop-color="#f3dcc0" stop-opacity=".75"/>
        <stop offset=".5" stop-color="#c99468" stop-opacity=".4"/>
        <stop offset="1" stop-color="#c99468" stop-opacity="0"/>
      </radialGradient>
      <radialGradient id="swirlGlowBack" cx=".5" cy=".5" r=".5">
        <stop offset="0" stop-color="#cf9d68" stop-opacity=".45"/>
        <stop offset="1" stop-color="#cf9d68" stop-opacity="0"/>
      </radialGradient>
    </defs>
    <g clip-path="url(#leftPanel)">
      <rect width="862" height="170" fill="var(--cocoa)"/>
      <g role="img" aria-label="Photo: lit candles resting on smooth spa stones">
        <rect y="170" width="862" height="175" fill="url(#candleBase)"/>
        <rect y="170" width="862" height="175" fill="url(#candleGlow)"/>
      </g>
      <rect y="345" width="862" height="70" fill="var(--tan)"/>
      <rect y="415" width="862" height="143" fill="var(--cocoa)"/>
      <ellipse cx="430" cy="490" rx="75" ry="65" fill="url(#swirlGlowBack)" role="img" aria-label="Tan swirl ornament"/>
    </g>
    <path d="M432,0 C395,45 385,120 420,195 C470,300 535,370 528,460 C524,510 500,540 470,558" fill="none" stroke="var(--tan)" stroke-width="4"/>
  </svg>

  <h2 class="txt back__title">Finest Home Visit<br>Massages</h2>
  <div class="txt back__aroma">AROMATHERAPY with Essential Oils</div>
  <div class="txt back__help">Help With Insomnia, Stress, Anxiety</div>
  <div class="txt back__signature">Tessa Coraline Whitby</div>
  <blockquote class="testimonial">
    <span class="testimonial__mark">&ldquo;</span>
    <p>She is extremely dedicated to the art of massage and healing.<br>Her talent and enthusiasm keep her clients coming back.<br>Tessa is always striving to improve techniques, surroundings<br>and her clients' overall experience.<br>- Thank you Tessa and Calm Haven for providing<br>exceptional service.</p>
  </blockquote>

  <div class="txt back__contact-name">Tessa Coraline Whitby</div>
  <div class="txt back__contact">Contact me on
    <svg width="18" height="18" viewBox="0 0 18 18"><circle cx="9" cy="9" r="8" fill="none" stroke="#6b4336" stroke-width="1.3"/><path d="M6 5c-1 1 0 4 2 6s5 3 6 2l-1.5-1.5-1.5 1c-1-.5-2.5-2-3-3l1-1.5z" fill="#6b4336"/></svg>
    000 0000 000</div>
  <div class="stamp-box"></div>
  <div class="address-line" style="top:245px"></div>
  <div class="address-line" style="top:286px"></div>
  <div class="address-line" style="top:327px"></div>
  <div class="address-line" style="top:368px"></div>
  <div class="address-line" style="top:409px"></div>
</section>

</body>
</html>
```